Kelvora Ledger Web Design Contest

We would like for you to design a website for www.kelvoraledger-example.com. Kelvora Ledger is a CPA Firm offering accounting, auditing, and tax preparation services.

We would like to have a consistent feel with the logo, business card, envelope, and stationary designs that were created by another designer on PlanHive. Examples of each are attached. We would like the website to have a clean/modern style.

The website should include the following:

1. A general "Welcome" landing page
2. A "About the Company" page
3. A "Services Offered" page
4. A "Contact Us" form
5. A button for "Sign up for Newsletter"

Target Market(s)

Individuals and businesses that require accounting, auditing, and tax preparation services from a CPA.

Industry/Entity Type

Accounting

Coding

Number of Pages Required

5+ page

Font styles to use
Other font styles liked:
• Trebuchet or similar

Requirements
Must have
• Consistent feel with logo and letterhead. The gray and blue bar on the letterhead should be incorporated into the website design.

```html
<!DOCTYPE html>
<html lang="en">
<head>
<meta charset="utf-8">
<title>Kelvora Ledger</title>
<link rel="stylesheet" href="https://fonts.googleapis.com/css2?family=Raleway:wght@400;500;600;700&family=Open+Sans:wght@400;600;700&display=swap">
<style>
:root{
  --navy:#0e1f4f;
  --navy-dark:#081536;
  --navy-deep:#06102c;
  --white:#ffffff;
  --light:#f1f1f3;
  --text:#555a66;
  --muted:#8a8f99;
  --heading:#20242c;
  --hero-a:#3a3d42;
  --hero-b:#9a9c9f;
  --band-a:#2a2c30;
  --band-b:#6d6f72;
}
*{margin:0;padding:0;box-sizing:border-box}
html,body{width:724px;height:1200px;overflow:hidden}
body{font-family:"Open Sans",Arial,sans-serif;color:var(--text);background:var(--white)}
.page{position:relative;width:724px;height:1200px}

.site-header{position:absolute;top:0;left:0;width:724px;height:68px;display:flex;justify-content:space-between;background:var(--white)}
.brand{display:flex;align-items:center;gap:8px;padding-left:20px}
.brand-box{width:30px;height:30px;background:var(--navy)}
.brand-name{font-family:"Raleway",sans-serif;font-weight:700;font-size:12px;color:var(--navy);letter-spacing:.5px}
.main-nav{display:flex;background:var(--navy);height:68px;width:338px}
.main-nav a{flex:1;display:flex;align-items:center;justify-content:center;color:var(--white);font-size:7.5px;font-weight:600;letter-spacing:.4px;text-decoration:none;text-align:center}
.main-nav a.active{background:var(--navy-dark)}

.hero{position:absolute;top:68px;left:0;width:724px;height:337px;background:linear-gradient(110deg,var(--hero-a) 0%,#5c5f63 45%,var(--hero-b) 100%);color:var(--white);text-align:center}
.hero-title{position:absolute;top:92px;width:100%;font-family:"Raleway",sans-serif;font-weight:700;font-size:46px;letter-spacing:2px}
.hero-rule{position:absolute;top:158px;left:0;width:100%;height:1px;background:rgba(255,255,255,.6)}
.hero-sub{position:absolute;top:172px;width:100%;font-family:"Raleway",sans-serif;font-weight:500;font-size:31px;line-height:40px}
.hero-dots{position:absolute;top:280px;width:100%;display:flex;justify-content:center;gap:6px}
.hero-dots span{width:8px;height:8px;border-radius:50%;background:var(--white)}

.welcome{position:absolute;top:405px;left:0;width:724px;height:148px;background:var(--light);text-align:center;padding-top:30px}
.welcome h2{font-family:"Raleway",sans-serif;font-weight:500;font-size:17px;color:var(--heading);letter-spacing:.5px}
.welcome p{width:540px;margin:14px auto 0;font-size:7px;line-height:11px;color:var(--muted)}
.btn-outline{display:inline-block;margin-top:12px;padding:5px 14px;border:1px solid var(--heading);font-size:6.5px;font-weight:600;color:var(--heading)}

.services{position:absolute;top:572px;left:28px;width:668px;display:flex;justify-content:space-between}
.service{width:206px}
.service-photo{width:206px;height:118px}
.photo-accounting{background:linear-gradient(135deg,#dfe6ea,#8eb0c4)}
.photo-auditing{background:linear-gradient(135deg,#f2f4f7,#9fb3cc)}
.photo-tax{background:linear-gradient(135deg,#f4f4f4,#bdbdbd)}
.service h3{margin-top:14px;font-size:9px;font-weight:700;color:var(--heading)}
.service p{margin-top:5px;font-size:6.5px;line-height:10px;color:var(--muted)}
.read-more{display:block;margin-top:8px;font-size:6.5px;font-weight:700;color:var(--heading)}

.motto{position:absolute;top:810px;left:0;width:724px;height:232px;background:linear-gradient(100deg,var(--band-a),var(--band-b) 60%,#3e4044);color:var(--white);text-align:center;padding-top:74px}
.motto-line{font-family:"Raleway",sans-serif;font-size:31px;line-height:38px}
.motto-line.strong{font-weight:700}
.motto-line.light{font-weight:500}

.newsletter{position:absolute;top:1042px;left:0;width:724px;height:68px;display:flex;align-items:center;padding:0 36px}
.newsletter-label{display:flex;align-items:center;gap:12px;font-family:"Raleway",sans-serif;font-size:14px;color:var(--heading);width:272px}
.newsletter-form{display:flex;gap:10px}
.newsletter-input{width:264px;height:28px;border:1px solid #cfd2d8;font-size:7px;color:var(--muted);padding:0 8px;display:flex;align-items:center}
.newsletter-btn{width:68px;height:28px;background:var(--navy);color:var(--white);font-size:9px;display:flex;align-items:center;justify-content:center}

.site-footer{position:absolute;top:1110px;left:0;width:724px;height:76px;background:var(--navy);color:var(--white);display:flex;justify-content:space-between;align-items:center;padding:0 40px}
.contact-list{list-style:none;font-size:7px;line-height:18px}
.contact-list li{display:flex;align-items:center;gap:8px}
.contact-list b{width:60px;font-weight:700}
.socials{display:flex;gap:12px}
.socials span{width:32px;height:32px;border-radius:50%;background:var(--white)}
.socials span.active{background:var(--navy-dark);border:2px solid var(--white)}

.legal{position:absolute;top:1186px;left:0;width:724px;height:14px;background:var(--navy-deep);color:var(--white);font-size:5.5px;display:flex;align-items:center;justify-content:center}
</style>
</head>
<body>
<div class="page">
  <header class="site-header">
    <div class="brand"><span class="brand-box"></span><span class="brand-name">KELVORA LEDGER, LLC</span></div>
    <nav class="main-nav">
      <a class="active">HOME</a><a>ABOUT THE COMPANY</a><a>SERVICES OFFERED</a><a>CONTACT US</a>
    </nav>
  </header>

  <section class="hero" role="img" aria-label="Photo of business people working together at an office desk">
    <h1 class="hero-title">GUIDE</h1>
    <div class="hero-rule"></div>
    <p class="hero-sub">YOUR BUSINESS IN THE<br>RIGHT DIRECTION!</p>
    <div class="hero-dots"><span></span><span></span></div>
  </section>

  <section class="welcome">
    <h2>WELCOME TO KELVORA LEDGER</h2>
    <p>We help individuals and growing businesses keep clear books, meet every filing date and plan ahead with confidence. Our certified accountants bring careful audits, honest advice and friendly service to every client we work with.</p>
    <span class="btn-outline">READ MORE</span>
  </section>

  <section class="services">
    <article class="service">
      <div class="service-photo photo-accounting" role="img" aria-label="Photo of hands using a calculator over financial papers"></div>
      <h3>Accounting</h3>
      <p>Monthly bookkeeping, payroll and clear financial statements for your firm.</p>
      <span class="read-more">READ MORE</span>
    </article>
    <article class="service">
      <div class="service-photo photo-auditing" role="img" aria-label="Photo of a pen reviewing printed charts"></div>
      <h3>Auditing</h3>
      <p>Independent audits and reviews that give lenders and owners real trust.</p>
      <span class="read-more">READ MORE</span>
    </article>
    <article class="service">
      <div class="service-photo photo-tax" role="img" aria-label="Photo of a clock face marked time for taxes"></div>
      <h3>Tax Preparation</h3>
      <p>Careful tax returns and planning for individuals and small businesses.</p>
      <span class="read-more">READ MORE</span>
    </article>
  </section>

  <section class="motto" role="img" aria-label="Dark photo of business people shaking hands">
    <p class="motto-line strong">UNION WITH US</p>
    <p class="motto-line light">IS YOUR WAY TO SUCCESS</p>
  </section>

  <section class="newsletter">
    <div class="newsletter-label">
      <svg width="18" height="13" viewBox="0 0 18 13"><rect x="0.75" y="0.75" width="16.5" height="11.5" fill="none" stroke="#0e1f4f" stroke-width="1.5"/><path d="M1 1l8 6 8-6" fill="none" stroke="#0e1f4f" stroke-width="1.5"/></svg>
      Subscribe to Our Newsletter
    </div>
    <div class="newsletter-form">
      <div class="newsletter-input">Enter Email</div>
      <div class="newsletter-btn">Subscribe</div>
    </div>
  </section>

  <footer class="site-footer">
    <ul class="contact-list">
      <li><svg width="8" height="10" viewBox="0 0 8 10"><path d="M4 0a4 4 0 0 1 4 4c0 3-4 6-4 6S0 7 0 4a4 4 0 0 1 4-4z" fill="#fff"/><circle cx="4" cy="4" r="1.5" fill="#0e1f4f"/></svg><b>ADDRESS</b>: Address Line1, Address Line2<br></li>
      <li style="margin-top:-8px;padding-left:76px">Country - 123456</li>
      <li><svg width="8" height="10" viewBox="0 0 8 10"><path d="M1 0h2l1 3-1.5 1a6 6 0 0 0 2.5 3l1-1.5 2 1v2.5C3 9 0 5 1 0z" fill="#fff"/></svg><b>FREE CALL</b>: 0800 123 4567</li>
      <li><svg width="8" height="10" viewBox="0 0 8 10"><rect x="0" y="2" width="8" height="6" fill="#fff"/><path d="M0 2l4 3 4-3" fill="none" stroke="#0e1f4f" stroke-width="0.8"/></svg><b>EMAIL ID</b>: info@companyname.com</li>
    </ul>
    <div class="socials"><span></span><span class="active"></span><span></span><span></span></div>
  </footer>

  <div class="legal">Kelvora Ledger © 2015 Privacy Policy Terms of use</div>
</div>
</body>
</html>
```